Website redesign for KestrelFinPro/TrailCoinPal

Job Title: Talented Web Designer for SEO-Friendly Website Creation & HostMarlow cPanel Integration
 
Inspiration: dunerevtrack.example
Pages:

About
Get a Quote
FAQ
Boat Loans
RV Loans
Testimonials
News/Blog
Affiliate Program
Contact

Job Description:
 
We are seeking a skilled and creative freelance web designer to build a stunning, SEO-optimized website for our business. The ideal candidate will have a strong design portfolio, technical expertise in creating search engine-friendly websites, and experience implementing websites into HostMarlow cPanel.
 
Project Overview:
 
Objective: Create a modern, motorsports themed visually appealing website that is optimized for SEO.

Platform: The site will be hosted on HostMarlow, so familiarity with their cPanel for setup and integration is essential.

Deliverables:
         •A fully functional website (desktop and mobile) with user-friendly navigation and a responsive design.
         •SEO best practices implemented throughout, including proper meta tags, optimized images, fast loading speeds, and mobile compatibility.
         •Seamless integration into HostMarlow cPanel for hosting.
         •Guidance or documentation on maintaining the site post-launch.
 
Key Skills Required:
 
         •Proficiency in web design (HTML, CSS, JavaScript, or relevant platforms like WordPress).
         •Knowledge of SEO principles and tools for website optimization.
         •Experience with HostMarlow cPanel, including file management and DNS settings.
         •Strong communication skills to understand our vision and provide progress updates.
 
What We’re Looking For:
 
         •A designer who can transform our ideas into a sleek and functional website.
         •Someone proactive in suggesting creative design elements and SEO improvements.
         •A reliable professional who can meet deadlines and deliver a polished product.
 
Please provide:
 
         1.A brief introduction and why you’re a good fit for this project.
         2.Examples of previous web design projects, especially those with SEO implementation.
         3.Your estimated timeline and cost for this project.
 
We are excited to work with a talented designer who can bring our vision to life. If you are passionate about web design and SEO, we’d love to hear from you!

Target Market(s)

Boat and RV buyers looking for a loan

Coding

Number of Pages Required

5+ page

Colors
F0912C
F2A743
F7CA91
FBE8D2
FDF5EE

Requirements
Must have
• motorsports type design
Nice to have
• fcontact forms easy to use layout on brand and color scheme of kestrelfinpro and trailcoinpal.example

```html
<!DOCTYPE html>
<html lang="en">
<head>
<meta charset="utf-8">
<title>KestrelFinPro – Boat Loans Made Easy</title>
<link rel="stylesheet" href="https://fonts.googleapis.com/css2?family=Barlow+Condensed:ital,wght@0,700;0,800;1,700;1,800&family=Bebas+Neue&family=DM+Sans:ital,wght@0,400;0,500;0,700;1,400&display=swap">
<style>
:root{
  --orange:#ff6a0c;
  --orange-deep:#f25a00;
  --orange-soft:#ff8a33;
  --blue:#0a86e4;
  --ink:#1f1f1f;
  --text:#6d6d6d;
  --line:#d6d6d6;
  --paper:#ffffff;
  --mist:#f2f2f2;
  --night:#050505;
}
*{box-sizing:border-box;margin:0;padding:0}
html,body{width:1200px;height:5106px;overflow:hidden}
body{position:relative;font-family:"DM Sans",sans-serif;color:var(--text);background:var(--paper)}
.abs{position:absolute}
.btn{display:inline-flex;align-items:center;justify-content:center;font-family:"Barlow Condensed",sans-serif;font-weight:700;font-size:14px;letter-spacing:.3px;color:#fff;text-transform:uppercase;border-radius:3px}
.btn--blue{background:var(--blue)}
.btn--orange{background:var(--orange)}
.sec-title{position:absolute;left:0;width:1200px;text-align:center;font-family:"Barlow Condensed",sans-serif;font-weight:800;font-style:italic;font-size:46px;line-height:1;text-transform:uppercase}
.sec-title .a{color:var(--blue)}
.sec-title .b{color:var(--orange)}
.brand{font-family:"Barlow Condensed",sans-serif;font-weight:800;color:var(--orange);text-transform:uppercase;display:inline-flex;align-items:center;gap:8px}
.brand .dot{width:14px;height:14px;border-radius:50%;background:var(--orange)}

/* top bar + header */
.topbar{left:278px;top:0;width:922px;height:44px;background:var(--orange);clip-path:polygon(22px 0,100% 0,100% 100%,0 100%);display:flex;align-items:center;padding-left:44px;gap:22px;color:#fff;font-size:13px}
.topbar .socials{margin-left:auto;margin-right:24px;display:flex;gap:8px}
.topbar .socials span{width:34px;height:34px;border:2px solid #fff;border-radius:50%}
.logo-main{left:28px;top:42px;font-size:32px}
.nav{left:288px;top:72px;display:flex;gap:32px;font-size:14px;color:#333}
.header-cta{left:928px;top:62px;display:flex;gap:8px}
.header-cta .btn{height:39px;padding:0 22px}

/* hero */
.hero{left:0;top:119px;width:1200px;height:575px;background:linear-gradient(180deg,#8ea4b8 0%,#b9c6d1 45%,#9a9a96 72%,#c9c7c2 100%);clip-path:polygon(0 0,100% 0,100% 92%,80% 97%,55% 94%,30% 99%,0 94%)}
.hero h1{position:absolute;top:72px;width:100%;text-align:center;font-family:"Bebas Neue",sans-serif;font-weight:400;font-size:92px;line-height:1;color:#fff;letter-spacing:1px}
.hero p{position:absolute;top:168px;width:100%;text-align:center;color:#fff;font-size:15px}
.hero .btn{position:absolute;left:543px;top:206px;width:115px;height:40px;font-size:13px}

/* why choose */
.why-title{top:790px}
.why-photo{top:886px;width:446px;height:314px}
.why-photo--boat{left:143px;background:linear-gradient(180deg,#aebfcb 0%,#8c9aa3 40%,#b3263a 60%,#2d2f33 100%)}
.why-photo--rv{left:609px;background:linear-gradient(180deg,#8fa9c4 0%,#c9ccd0 45%,#6b5848 75%,#6f7a5a 100%)}
.why-brand{top:1222px;width:446px;justify-content:center;font-size:28px}
.why-text{top:1266px;width:446px;text-align:center;font-size:14px;line-height:28px}

/* about */
.about{left:0;top:1438px;width:1200px;height:476px;background:linear-gradient(100deg,var(--orange-deep),var(--orange) 55%,var(--orange-soft));clip-path:polygon(0 10%,30% 4%,60% 8%,100% 0,100% 92%,70% 100%,40% 95%,0 100%)}
.about-boat{left:20px;top:1560px;width:575px;height:330px;border-radius:48% 40% 46% 50%/40% 30% 60% 55%;background:linear-gradient(170deg,#f1f3f5 0%,#c8cfd5 55%,#7d868e 100%)}
.about-title{left:601px;top:1566px;font-family:"Barlow Condensed",sans-serif;font-weight:800;font-style:italic;font-size:44px;color:#fff;text-transform:uppercase;line-height:1}
.about-text{left:601px;top:1626px;width:460px;color:#fff;font-size:13.5px;line-height:28px}
.about .btn,.about-btn{left:601px;top:1782px;width:120px;height:40px}

/* testimonials */
.testi-title{top:2008px}
.card{position:absolute;width:293px;height:296px;background:#fff;box-shadow:0 2px 10px rgba(0,0,0,.12);padding:22px 22px 0 22px}
.card q{display:block;font-style:italic;font-size:13px;line-height:28px;color:var(--text);quotes:none}
.card .who{position:absolute;left:22px;bottom:22px;display:flex;align-items:center;gap:10px}
.card .avatar{width:46px;height:46px;border-radius:50%;background:linear-gradient(160deg,#b99377,#6e5648)}
.card .name{font-family:"Barlow Condensed",sans-serif;font-weight:700;font-size:16px;color:var(--ink);text-transform:uppercase}
.card .stars{color:#ffb300;font-size:13px;letter-spacing:1px}
.arrow{position:absolute;width:30px;height:30px}

/* affiliate */
.affiliate{left:0;top:2840px;width:1200px;height:327px;background:linear-gradient(90deg,#ff6d0e,#ff7f22 50%,#ff6a0a)}
.aff-title{top:2932px;color:#fff}
.badge{position:absolute;top:3014px;width:161px;height:74px;background:#fff;border-radius:3px;display:flex;align-items:center;justify-content:center}
.badge span{width:90px;height:34px;background:#c9ccd1;border-radius:6px}

/* blog */
.blog-title{top:3290px}
.post{position:absolute;top:3371px;width:296px;height:440px;background:#fff;box-shadow:0 2px 10px rgba(0,0,0,.12)}
.post .photo{height:250px}
.post .panel{position:absolute;left:16px;right:16px;top:214px;background:#fff;padding:10px 10px 0;text-align:center}
.post h3{font-family:"Barlow Condensed",sans-serif;font-weight:800;font-style:italic;font-size:21px;line-height:30px;color:var(--ink);text-transform:uppercase}
.post p{margin-top:8px;font-size:13px;line-height:27px}
.post .btn{margin-top:16px;width:118px;height:39px}

/* quote */
.quote{left:0;top:3936px;width:1200px;height:640px;background:var(--mist)}
.quote-title{top:4040px}
.quote-lead{left:190px;top:4096px;width:820px;text-align:center;font-size:13px;line-height:28px}
.field{position:absolute;background:#fff;border:1px solid var(--line);font-size:13px;color:#888;padding:0 16px;display:flex;align-items:center}
.field--area{align-items:flex-start;padding-top:16px}
.submit{left:541px;top:4440px;width:119px;height:38px}

/* footer */
.footer{left:0;top:4541px;width:1200px;height:565px;background:var(--night);clip-path:polygon(0 8%,15% 3%,35% 9%,55% 2%,75% 8%,100% 3%,100% 100%,0 100%)}
.foot-brand{left:0;top:4696px;width:1200px;justify-content:center;font-size:36px}
.foot-nav{left:0;top:4772px;width:1200px;display:flex;justify-content:center;gap:36px;color:#fff;font-size:14px}
.rule{position:absolute;left:160px;width:880px;height:1px;background:#3a3a3a}
.vrule{position:absolute;top:4886px;width:1px;height:60px;background:#3a3a3a}
.contact{position:absolute;top:4886px;display:flex;align-items:center;gap:12px}
.contact .pin{width:62px;height:62px;border-radius:50%;background:var(--blue);display:flex;align-items:center;justify-content:center}
.contact .label{font-family:"Barlow Condensed",sans-serif;font-weight:700;color:var(--orange);font-size:15px;text-transform:uppercase}
.contact .val{color:#fff;font-size:14px;line-height:22px}
.copy{left:0;top:5018px;width:1200px;text-align:center;color:#fff;font-size:13px}
.copy b{color:var(--orange);font-weight:700}
</style>
</head>
<body>

<header>
  <div class="abs brand logo-main"><span class="dot"></span>KestrelFinPro.com</div>
  <div class="abs topbar">
    <span>★ Based on 1606 reviews</span>
    <span>Call us today: 555-014-7720</span>
    <span>Email us : reed@kestrelfinpro.example</span>
    <div class="socials" aria-label="Social profiles"><span></span><span></span><span></span><span></span></div>
  </div>
  <nav class="abs nav">
    <span>About</span><span>FAQ</span><span>Boat Loans</span><span>RV Loans</span><span>Testimonials</span><span>Blog</span><span>Affiliate Program</span>
  </nav>
  <div class="abs header-cta"><span class="btn btn--blue">Contact Us</span><span class="btn btn--orange">Get a Quote</span></div>
</header>

<section class="abs hero" role="img" aria-label="Grey pickup truck towing a pontoon boat on a trailer along a waterfront road under a cloudy sky">
  <h1>BOAT LOANS MADE EASY!</h1>
  <p>Welcome to KestrelFinPro.com, your one-stop resource for all of your boat financing needs.</p>
  <span class="btn btn--orange">Get a Quote</span>
</section>

<h2 class="sec-title why-title"><span class="a">Why </span><span class="b">Choose Us</span></h2>
<div class="abs why-photo why-photo--boat" role="img" aria-label="Red and black performance boat on a lake"></div>
<div class="abs why-photo why-photo--rv" role="img" aria-label="Large motorhome parked outdoors"></div>
<div class="abs brand why-brand" style="left:143px">KestrelFinPro.com</div>
<div class="abs brand why-brand" style="left:609px">TrailCoinPal.com</div>
<p class="abs why-text" style="left:143px">Our goal is to make your boat purchase as quick and stress-free as possible. Our numerous lender relationships Allow us to offer competitive rates and terms with quick turn-around times.</p>
<p class="abs why-text" style="left:609px">Our goal is to make your RV purchase as quick and stress-free as possible. Our numerous lender relationships allow us to offer competitive rates and terms with quick turn-around times.</p>

<section class="abs about"></section>
<div class="abs about-boat" role="img" aria-label="White wake-surf boat with tower, side view"></div>
<h2 class="abs about-title">About Us</h2>
<p class="abs about-text">Loans from $25,000 - $5M, Up to 25yrs old, Same-Day Approvals, Quick Funding, Private Party or Dealer, Best Rates in the Industry<br>Our goal is to make your boat purchase as quick and stress-free as possible. Our numerous lender relationships Allow us to offer competitive rates and terms with quick turn-around times.</p>
<span class="abs btn btn--blue about-btn">Learn More</span>

<h2 class="sec-title testi-title"><span class="a">Our Client </span><span class="b">Testimonials</span></h2>
<svg class="arrow" style="left:136px;top:2222px" viewBox="0 0 30 30" aria-hidden="true"><path d="M19 5 9 15l10 10" fill="none" stroke="#111" stroke-width="3.5"/></svg>
<svg class="arrow" style="left:1032px;top:2533px" viewBox="0 0 30 30" aria-hidden="true"><path d="M11 5l10 10-10 10" fill="none" stroke="#111" stroke-width="3.5"/></svg>

<article class="card" style="left:198px;top:2088px"><q>"Just purchased a boat and used Harborline and they made the process very easy. Dana Whitlow helped every step of the way and was always available when I had any questions. She was quick to keep me updated and streamlined the entire process"</q><div class="who"><span class="avatar"></span><div><div class="name">Owen Mercer</div><div class="stars">★★★★★</div></div></div></article>
<article class="card" style="left:510px;top:2088px"><q>"I have nothing but outstanding things to say about Dana. From my initial phone call in March, I knew that I was in good hands. Always there to answer all my questions either through text or a phone call. Even answering before and after business."</q><div class="who"><span class="avatar"></span><div><div class="name">Owen Mercer</div><div class="stars">★★★★★</div></div></div></article>
<article class="card" style="left:821px;top:2088px"><q>"Harborline Recreational Finance (HRF) was awesome to work with. Both Miles Corra and Evan Lusk were wonderful but Evan went above and beyond to make things happen quickly. He was always available and on top of everything. Evan had to go."</q><div class="who"><span class="avatar"></span><div><div class="name">Owen Mercer</div><div class="stars">★★★★★</div></div></div></article>
<article class="card" style="left:87px;top:2401px"><q>"Just purchased a boat and used Harborline and they made the process very easy. Dana Whitlow helped every step of the way and was always available when I had any questions. She was quick to keep me updated and streamlined the entire process"</q><div class="who"><span class="avatar"></span><div><div class="name">Owen Mercer</div><div class="stars">★★★★★</div></div></div></article>
<article class="card" style="left:397px;top:2401px"><q>"I have nothing but outstanding things to say about Dana. From my initial phone call in March, I knew that I was in good hands. Always there to answer all my questions either through text or a phone call. Even answering before and after business."</q><div class="who"><span class="avatar"></span><div><div class="name">Owen Mercer</div><div class="stars">★★★★★</div></div></div></article>
<article class="card" style="left:708px;top:2401px"><q>"Harborline Recreational Finance (HRF) was awesome to work with. Both Miles Corra and Evan Lusk were wonderful but Evan went above and beyond to make things happen quickly. He was always available and on top of everything. Evan had to go."</q><div class="who"><span class="avatar"></span><div><div class="name">Owen Mercer</div><div class="stars">★★★★★</div></div></div></article>

<section class="abs affiliate" role="img" aria-label="Orange-tinted marina with docked boats"></section>
<h2 class="sec-title aff-title">Affiliate Program</h2>
<div class="badge" style="left:174px" aria-label="Partner badge"><span></span></div>
<div class="badge" style="left:347px" aria-label="Partner badge"><span></span></div>
<div class="badge" style="left:520px" aria-label="Partner badge"><span style="width:50px;height:50px;border-radius:50%"></span></div>
<div class="badge" style="left:692px" aria-label="Partner badge"><span></span></div>
<div class="badge" style="left:865px" aria-label="Partner badge"><span></span></div>

<h2 class="sec-title blog-title"><span class="a">Our News </span><span class="b">&amp; Blog</span></h2>
<article class="post" style="left:135px"><div class="photo" role="img" aria-label="Speedboat racing across a lake near desert hills" style="background:linear-gradient(180deg,#9fc4e0 0%,#b59a78 40%,#3e7fa8 70%,#1f5f88 100%)"></div><div class="panel"><h3>Lorem ipsum dolorsit amet consectetur.</h3><p>Lorem ipsum dolor sit amet, consectetur adipiscing elit, sed do eiusmod tempor incididunt ut.</p><span class="btn btn--blue">Learn More</span></div></article>
<article class="post" style="left:452px"><div class="photo" role="img" aria-label="Dark performance boat with red accents on the water" style="background:linear-gradient(180deg,#5f7f90 0%,#2c3a42 50%,#3f6270 100%)"></div><div class="panel"><h3>Lorem ipsum dolorsit amet consectetur.</h3><p>Lorem ipsum dolor sit amet, consectetur adipiscing elit, sed do eiusmod tempor incididunt ut.</p><span class="btn btn--blue">Learn More</span></div></article>
<article class="post" style="left:769px"><div class="photo" role="img" aria-label="Green and black powerboat on a dark lake" style="background:linear-gradient(180deg,#7a8c80 0%,#3a4a40 45%,#27b04a 65%,#1c2a2a 100%)"></div><div class="panel"><h3>Lorem ipsum dolorsit amet consectetur.</h3><p>Lorem ipsum dolor sit amet, consectetur adipiscing elit, sed do eiusmod tempor incididunt ut.</p><span class="btn btn--blue">Learn More</span></div></article>

<section class="abs quote"></section>
<h2 class="sec-title quote-title"><span class="a">Request </span><span class="b">a Quote</span></h2>
<p class="abs quote-lead">Lorem ipsum dolor sit amet, consectetur adipiscing elit, sed do eiusmod tempor incididunt ut labore et dolore magna aliquasuspendisse ultrices gravidasus commodo viverra maecenas accumsan lacus vel facilisis.</p>
<div class="field" style="left:254px;top:4170px;width:339px;height:44px">First Name</div>
<div class="field" style="left:611px;top:4170px;width:333px;height:44px">Last Name</div>
<div class="field" style="left:254px;top:4232px;width:339px;height:44px">Email Address</div>
<div class="field" style="left:611px;top:4232px;width:333px;height:44px">Phone Number</div>
<div class="field field--area" style="left:254px;top:4295px;width:690px;height:119px">Message</div>
<span class="abs btn btn--blue submit">Submit Now</span>

<footer class="abs footer"></footer>
<div class="abs brand foot-brand"><span class="dot"></span>KestrelFinPro.com</div>
<nav class="abs foot-nav"><span>About</span><span>FAQ</span><span>Boat Loans</span><span>RV Loans</span><span>Testimonials</span><span>Blog</span><span>Affiliate Program</span><span>Get A Quote</span><span>Contact us</span></nav>
<div class="rule" style="top:4832px"></div>
<div class="contact" style="left:158px"><span class="pin"><svg width="20" height="24" viewBox="0 0 20 24" aria-hidden="true"><path d="M10 1a8 8 0 0 0-8 8c0 6 8 14 8 14s8-8 8-14a8 8 0 0 0-8-8z" fill="#fff"/><circle cx="10" cy="9" r="3" fill="#0a86e4"/></svg></span><div><div class="label">Address</div><div class="val">4410 Harbor Crest Drive<br>Ste. 210, Bayview, CA 90000</div></div></div>
<div class="vrule" style="left:480px"></div>
<div class="contact" style="left:524px"><span class="pin"><svg width="20" height="24" viewBox="0 0 20 24" aria-hidden="true"><path d="M10 1a8 8 0 0 0-8 8c0 6 8 14 8 14s8-8 8-14a8 8 0 0 0-8-8z" fill="#fff"/><circle cx="10" cy="9" r="3" fill="#0a86e4"/></svg></span><div><div class="label">Call Us</div><div class="val">(555) 014-7720</div></div></div>
<div class="vrule" style="left:753px"></div>
<div class="contact" style="left:796px"><span class="pin"><svg width="20" height="24" viewBox="0 0 20 24" aria-hidden="true"><path d="M10 1a8 8 0 0 0-8 8c0 6 8 14 8 14s8-8 8-14a8 8 0 0 0-8-8z" fill="#fff"/><circle cx="10" cy="9" r="3" fill="#0a86e4"/></svg></span><div><div class="label">Email Us</div><div class="val">reed@kestrelfinpro.example</div></div></div>
<div class="rule" style="top:4987px"></div>
<p class="abs copy">© copyrights 2024 <b>KestrelFinPro.</b> &nbsp; | &nbsp; Allrights Reserved</p>

</body>
</html>
```